Washing powder bag design.

Project Description – Graphic Design Proposal for ORNE Laundry Powder Packaging
We have already explored initial design ideas internally, supported by AI-assisted tools (ChatGPT) to develop early concepts, layouts, and mockups. To support this, we have attached the bag die-cut, where graphics and text are placed as a visual guideline for the intended structure. In addition, we have included a mockup of the product series currently under development to clearly communicate the desired style, direction, and overall visual identity.
The mockup should be regarded as the design foundation for this project and as a starting point for professional refinement.
Scope of Work
We would like you to create three graphic design variants, each based on a different color direction:
1. Variant 1: In line with our current color scheme
2. Variant 2: A blue version
3. Variant 3: A green version
Design Elements to Be Preserved
The following elements must be maintained across all three variants:
• The overall style and visual expression of the mockup
• The leaf-shaped element in the bottom right corner
• The ORNE layout, including typography, positioning, and general look & feel
Summary
While the color palette may vary, the structure, style, and key design elements must remain consistent and be directly based on the attached mockup.
We look forward to seeing your creative interpretation and professional input.
Updates
We need the design to be created based on the attached die-cut file “Orne 10 kg BAG 202526”, including all text elements.
We would like the final to include both the designed die-cut file and a mockup.

```html
<!DOCTYPE html>
<html lang="da">
<head>
<meta charset="utf-8">
<title>ORNE Vaskepulver – emballagevarianter</title>
<link rel="stylesheet" href="https://fonts.googleapis.com/css2?family=Montserrat:wght@500;600;700;800&display=swap">
<style>
  :root{
    --page:#f9faf4;
    --paper:#ffffff;
    --ink-soft:#3a3a3a;
    --warn:#d9262b;
  }
  *{box-sizing:border-box;margin:0;padding:0}
  html,body{width:1200px;height:1200px;overflow:hidden;background:var(--page)}
  body{position:relative;font-family:"Montserrat",sans-serif}

  .variant-green{--tint:#dfe9cf;--mark:#b9d89c;--dark:#2f4f1d;--label:#5f8a3a;--leaf:#c9dcb2}
  .variant-sage{--tint:#ece6d7;--mark:#cfdcbc;--dark:#1f4a38;--label:#93ab84;--leaf:#dcdcc6}
  .variant-blue{--tint:#cfe5ef;--mark:#8ad2ea;--dark:#0f4a63;--label:#1a7fa0;--leaf:#b4dcea}
  .variant-sand{--tint:#e9e1cd;--mark:#d8c8a4;--dark:#4a3f25;--label:#8c7a4f;--leaf:#dccfb2}

  .bag{position:absolute;overflow:hidden;border-radius:6px}
  .hole{position:absolute;border-radius:50%;background:var(--page)}

  /* Front panel 290 x 482 */
  .bag-front{width:290px;height:482px;background:linear-gradient(180deg,var(--paper) 0%,var(--paper) 18%,var(--tint) 60%,var(--tint) 100%)}
  .bag-front .hole{width:26px;height:26px;top:26px}
  .leaf-decor{position:absolute;right:-20px;bottom:-10px;width:150px;height:170px;border-radius:60% 10% 60% 10%;background:radial-gradient(circle at 60% 55%,var(--leaf) 0%,transparent 70%);opacity:.9}
  .brand-disc{position:absolute;left:60px;top:73px;width:162px;height:162px;border-radius:50%;background:var(--mark);display:flex;align-items:center;justify-content:center}
  .brand-name{font-weight:800;font-size:52px;letter-spacing:1px;color:var(--dark)}
  .product-title{position:absolute;left:0;width:100%;top:262px;text-align:center;font-weight:800;font-size:27px;color:var(--dark);letter-spacing:.3px}
  .product-sub{position:absolute;left:0;width:100%;top:295px;text-align:center;font-weight:700;font-size:14.5px;color:var(--label)}
  .claim-pill{position:absolute;left:56px;top:324px;width:171px;height:48px;border-radius:24px;background:var(--dark);box-shadow:0 0 0 3px var(--tint),0 0 0 5px var(--dark);color:#fff;font-weight:700;font-size:12.5px;line-height:16px;text-align:center;display:flex;align-items:center;justify-content:center}
  .feature-row{position:absolute;left:25px;top:406px;display:flex;gap:5px}
  .feature{width:44px;height:44px;border-radius:8px;background:var(--dark);display:flex;align-items:center;justify-content:center}
  .feature-inner{width:36px;height:36px;border-radius:5px;border:2px solid #fff;display:flex;align-items:center;justify-content:center;color:#fff;font-weight:700;font-size:13px}
  .weight-badge{position:absolute;left:199px;top:399px;width:64px;height:64px;border-radius:50%;background:var(--dark);box-shadow:inset 0 0 0 3px var(--dark),inset 0 0 0 5px #fff;color:#fff;display:flex;align-items:center;justify-content:center;font-weight:800;font-size:28px;letter-spacing:-2px}
  .weight-badge small{font-size:11px;letter-spacing:0;margin-left:2px;color:var(--mark)}
  .temps{position:absolute;left:25px;top:455px;font-weight:700;font-size:10.5px;color:var(--dark)}

  /* Back panel 183 x 305 */
  .bag-back{width:183px;height:305px;background:var(--tint)}
  .bag-back .hole{width:16px;height:16px;top:17px}
  .guide{position:absolute;left:15px;top:59px;width:67px;height:229px;background:#fff;border:1px solid #333;padding:2px;font-size:3.4px;line-height:4.4px;color:var(--ink-soft);text-align:center}
  .guide h4{background:#222;color:#fff;font-size:3.2px;padding:1px;margin:2px 0;text-align:left}
  .warning{position:absolute;left:99px;top:58px;width:63px;height:91px;background:#fff;border:1px solid #333;font-size:3.2px;line-height:4.2px;color:var(--ink-soft);text-align:center;padding:2px}
  .warning h5{display:inline-block;background:#222;color:#fff;font-size:3.2px;padding:0 3px;border-radius:2px}
  .hazard{width:16px;height:16px;margin:5px auto 4px;border:1.6px solid var(--warn);transform:rotate(45deg);display:flex;align-items:center;justify-content:center}
  .hazard span{transform:rotate(-45deg);font-weight:800;font-size:9px;color:#111}
  .dosage-title{position:absolute;left:90px;width:82px;top:174px;text-align:center;font-weight:700;font-size:8.5px;line-height:9px;color:var(--dark)}
  .dosage-table{position:absolute;left:96px;top:198px;width:70px;border-collapse:collapse;font-size:3.6px;color:#222;background:transparent}
  .dosage-table td,.dosage-table th{border:.6px solid #555;padding:1px;text-align:center;font-weight:600}
  .dosage-table th{font-size:3.2px}
  .dosage-table .size{font-size:5px;font-weight:700}
  .mini-features{position:absolute;left:97px;top:266px;display:flex;gap:4px}
  .mini-features .feature{width:19px;height:19px;border-radius:4px}
  .mini-features .feature-inner{width:15px;height:15px;border-width:1px;border-radius:2px;font-size:5.5px}
  .mini-temps{position:absolute;left:96px;top:289px;font-weight:700;font-size:4.4px;color:var(--dark)}
</style>
</head>
<body>

<!-- Green -->
<section class="bag bag-back variant-green" style="left:59px;top:158px">
  <span class="hole" style="left:59px"></span><span class="hole" style="left:84px"></span><span class="hole" style="left:109px"></span>
  <div class="guide">
    <h4>(DK) BRUGERVEJLEDNING – ORNE VASKEPULVER</h4>
    <p>Til universal brug.</p><p>Egnet til alle typer tøj og maskiner.</p><p>Følg altid tøjets vaskeanvisning.</p><p>Dosering efter vandets hårdhed.</p><p>Opbevares tørt og utilgængeligt for børn.</p><p>Undgå kontakt med øjne og hud.</p>
    <h4>(GB) USER GUIDE – ORNE LAUNDRY DETERGENT POWDER</h4>
    <p>Universal detergent.</p><p>Suitable for all washable textiles.</p><p>Always follow the garment care label.</p><p>Dose according to water hardness.</p><p>Store dry and out of reach of children.</p><p>Avoid contact with eyes and skin.</p>
  </div>
  <div class="warning"><h5>Advarsel Warning</h5><div class="hazard"><span>!</span></div><p>Forårsager alvorlig øjenirritation. Causes serious eye irritation.</p><p>Keep out of reach of children.</p><p>UFI: 0000-0000-0000-0000</p></div>
  <div class="dosage-title">DOSERING<br>DOSAGE</div>
  <table class="dosage-table"><tr><th></th><th>soft</th><th>medium</th><th>hard</th></tr><tr><td class="size">1Kg</td><td>37 ml ≈41g</td><td>37 ml ≈61g</td><td>83 g</td></tr><tr><td class="size">5Kg</td><td>65 Kg</td><td>37 ml ≈83g</td><td>83 g</td></tr><tr><td class="size">10Kg</td><td>112 Kg</td><td>112 ml ≈124g</td><td>144g</td></tr><tr><td colspan="4">75 ml = 83g</td></tr></table>
  <div class="mini-features"><div class="feature"><div class="feature-inner">120</div></div><div class="feature"><div class="feature-inner"><svg width="9" height="9" viewBox="0 0 10 10"><circle cx="5" cy="5" r="3.6" fill="none" stroke="#fff" stroke-width="1.4"/></svg></div></div><div class="feature"><div class="feature-inner"><svg width="10" height="9" viewBox="0 0 20 18"><path d="M2 7h16l-2 9H4z M8 7l3-5 3 2" fill="none" stroke="#fff" stroke-width="1.8"/></svg></div></div></div>
  <div class="mini-temps">20°C | 30°C | 40°C | 60°C | 90°C</div>
</section>
<section class="bag bag-front variant-green" style="left:267px;top:47px">
  <span class="hole" style="left:94px"></span><span class="hole" style="left:133px"></span><span class="hole" style="left:171px"></span>
  <div class="leaf-decor" role="img" aria-label="Faint leaf decoration"></div>
  <div class="brand-disc"><span class="brand-name">ORNE</span></div>
  <h1 class="product-title">VASKEPULVER</h1>
  <p class="product-sub">LAUNDRY DETERGENT</p>
  <div class="claim-pill">LIV OG BALANCE<br>I HVERDAGEN</div>
  <div class="feature-row"><div class="feature"><div class="feature-inner">120</div></div><div class="feature"><div class="feature-inner"><svg width="20" height="20" viewBox="0 0 10 10"><circle cx="5" cy="5" r="3.6" fill="none" stroke="#fff" stroke-width="1.4"/></svg></div></div><div class="feature"><div class="feature-inner"><svg width="24" height="22" viewBox="0 0 20 18"><path d="M2 7h16l-2 9H4z M8 7l3-5 3 2" fill="none" stroke="#fff" stroke-width="1.5"/></svg></div></div></div>
  <div class="weight-badge">10<small>kg</small></div>
  <div class="temps">20°C | 30°C | 40°C | 60°C | 90°C</div>
</section>

<!-- Sage / current colours -->
<section class="bag bag-back variant-sage" style="left:655px;top:160px">
  <span class="hole" style="left:59px"></span><span class="hole" style="left:84px"></span><span class="hole" style="left:109px"></span>
  <div class="guide">
    <h4>(DK) BRUGERVEJLEDNING – ORNE VASKEPULVER</h4>
    <p>Til universal brug.</p><p>Egnet til alle typer tøj og maskiner.</p><p>Følg altid tøjets vaskeanvisning.</p><p>Dosering efter vandets hårdhed.</p><p>Opbevares tørt og utilgængeligt for børn.</p><p>Undgå kontakt med øjne og hud.</p>
    <h4>(GB) USER GUIDE – ORNE LAUNDRY DETERGENT POWDER</h4>
    <p>Universal detergent.</p><p>Suitable for all washable textiles.</p><p>Always follow the garment care label.</p><p>Dose according to water hardness.</p><p>Store dry and out of reach of children.</p><p>Avoid contact with eyes and skin.</p>
  </div>
  <div class="warning"><h5>Advarsel Warning</h5><div class="hazard"><span>!</span></div><p>Forårsager alvorlig øjenirritation. Causes serious eye irritation.</p><p>Keep out of reach of children.</p><p>UFI: 0000-0000-0000-0000</p></div>
  <div class="dosage-title">DOSERING<br>DOSAGE</div>
  <table class="dosage-table"><tr><th></th><th>soft</th><th>medium</th><th>hard</th></tr><tr><td class="size">1Kg</td><td>37 ml ≈41g</td><td>37 ml ≈61g</td><td>83 g</td></tr><tr><td class="size">5Kg</td><td>65 Kg</td><td>37 ml ≈83g</td><td>83 g</td></tr><tr><td class="size">10Kg</td><td>112 Kg</td><td>112 ml ≈124g</td><td>144g</td></tr><tr><td colspan="4">75 ml = 83g</td></tr></table>
  <div class="mini-features"><div class="feature"><div class="feature-inner">120</div></div><div class="feature"><div class="feature-inner"><svg width="9" height="9" viewBox="0 0 10 10"><circle cx="5" cy="5" r="3.6" fill="none" stroke="#fff" stroke-width="1.4"/></svg></div></div><div class="feature"><div class="feature-inner"><svg width="10" height="9" viewBox="0 0 20 18"><path d="M2 7h16l-2 9H4z M8 7l3-5 3 2" fill="none" stroke="#fff" stroke-width="1.8"/></svg></div></div></div>
  <div class="mini-temps">20°C | 30°C | 40°C | 60°C | 90°C</div>
</section>
<section class="bag bag-front variant-sage" style="left:863px;top:47px">
  <span class="hole" style="left:94px"></span><span class="hole" style="left:133px"></span><span class="hole" style="left:171px"></span>
  <div class="leaf-decor" role="img" aria-label="Faint leaf decoration"></div>
  <div class="brand-disc"><span class="brand-name">ORNE</span></div>
  <h1 class="product-title">VASKEPULVER</h1>
  <p class="product-sub">LAUNDRY DETERGENT</p>
  <div class="claim-pill">LIV OG BALANCE<br>I HVERDAGEN</div>
  <div class="feature-row"><div class="feature"><div class="feature-inner">120</div></div><div class="feature"><div class="feature-inner"><svg width="20" height="20" viewBox="0 0 10 10"><circle cx="5" cy="5" r="3.6" fill="none" stroke="#fff" stroke-width="1.4"/></svg></div></div><div class="feature"><div class="feature-inner"><svg width="24" height="22" viewBox="0 0 20 18"><path d="M2 7h16l-2 9H4z M8 7l3-5 3 2" fill="none" stroke="#fff" stroke-width="1.5"/></svg></div></div></div>
  <div class="weight-badge">10<small>kg</small></div>
  <div class="temps">20°C | 30°C | 40°C | 60°C | 90°C</div>
</section>

<!-- Blue -->
<section class="bag bag-back variant-blue" style="left:62px;top:760px">
  <span class="hole" style="left:59px"></span><span class="hole" style="left:84px"></span><span class="hole" style="left:109px"></span>
  <div class="guide">
    <h4>(DK) BRUGERVEJLEDNING – ORNE VASKEPULVER</h4>
    <p>Til universal brug.</p><p>Egnet til alle typer tøj og maskiner.</p><p>Følg altid tøjets vaskeanvisning.</p><p>Dosering efter vandets hårdhed.</p><p>Opbevares tørt og utilgængeligt for børn.</p><p>Undgå kontakt med øjne og hud.</p>
    <h4>(GB) USER GUIDE – ORNE LAUNDRY DETERGENT POWDER</h4>
    <p>Universal detergent.</p><p>Suitable for all washable textiles.</p><p>Always follow the garment care label.</p><p>Dose according to water hardness.</p><p>Store dry and out of reach of children.</p><p>Avoid contact with eyes and skin.</p>
  </div>
  <div class="warning"><h5>Advarsel Warning</h5><div class="hazard"><span>!</span></div><p>Forårsager alvorlig øjenirritation. Causes serious eye irritation.</p><p>Keep out of reach of children.</p><p>UFI: 0000-0000-0000-0000</p></div>
  <div class="dosage-title">DOSERING<br>DOSAGE</div>
  <table class="dosage-table"><tr><th></th><th>soft</th><th>medium</th><th>hard</th></tr><tr><td class="size">1Kg</td><td>37 ml ≈41g</td><td>37 ml ≈61g</td><td>83 g</td></tr><tr><td class="size">5Kg</td><td>65 Kg</td><td>37 ml ≈83g</td><td>83 g</td></tr><tr><td class="size">10Kg</td><td>112 Kg</td><td>112 ml ≈124g</td><td>144g</td></tr><tr><td colspan="4">75 ml = 83g</td></tr></table>
  <div class="mini-features"><div class="feature"><div class="feature-inner">120</div></div><div class="feature"><div class="feature-inner"><svg width="9" height="9" viewBox="0 0 10 10"><circle cx="5" cy="5" r="3.6" fill="none" stroke="#fff" stroke-width="1.4"/></svg></div></div><div class="feature"><div class="feature-inner"><svg width="10" height="9" viewBox="0 0 20 18"><path d="M2 7h16l-2 9H4z M8 7l3-5 3 2" fill="none" stroke="#fff" stroke-width="1.8"/></svg></div></div></div>
  <div class="mini-temps">20°C | 30°C | 40°C | 60°C | 90°C</div>
</section>
<section class="bag bag-front variant-blue" style="left:267px;top:647px">
  <span class="hole" style="left:94px"></span><span class="hole" style="left:133px"></span><span class="hole" style="left:171px"></span>
  <div class="leaf-decor" role="img" aria-label="Faint leaf decoration"></div>
  <div class="brand-disc"><span class="brand-name">ORNE</span></div>
  <h1 class="product-title">VASKEPULVER</h1>
  <p class="product-sub">LAUNDRY DETERGENT</p>
  <div class="claim-pill">LIV OG BALANCE<br>I HVERDAGEN</div>
  <div class="feature-row"><div class="feature"><div class="feature-inner">120</div></div><div class="feature"><div class="feature-inner"><svg width="20" height="20" viewBox="0 0 10 10"><circle cx="5" cy="5" r="3.6" fill="none" stroke="#fff" stroke-width="1.4"/></svg></div></div><div class="feature"><div class="feature-inner"><svg width="24" height="22" viewBox="0 0 20 18"><path d="M2 7h16l-2 9H4z M8 7l3-5 3 2" fill="none" stroke="#fff" stroke-width="1.5"/></svg></div></div></div>
  <div class="weight-badge">10<small>kg</small></div>
  <div class="temps">20°C | 30°C | 40°C | 60°C | 90°C</div>
</section>

<!-- Sand -->
<section class="bag bag-back variant-sand" style="left:665px;top:760px">
  <span class="hole" style="left:59px"></span><span class="hole" style="left:84px"></span><span class="hole" style="left:109px"></span>
  <div class="guide">
    <h4>(DK) BRUGERVEJLEDNING – ORNE VASKEPULVER</h4>
    <p>Til universal brug.</p><p>Egnet til alle typer tøj og maskiner.</p><p>Følg altid tøjets vaskeanvisning.</p><p>Dosering efter vandets hårdhed.</p><p>Opbevares tørt og utilgængeligt for børn.</p><p>Undgå kontakt med øjne og hud.</p>
    <h4>(GB) USER GUIDE – ORNE LAUNDRY DETERGENT POWDER</h4>
    <p>Universal detergent.</p><p>Suitable for all washable textiles.</p><p>Always follow the garment care label.</p><p>Dose according to water hardness.</p><p>Store dry and out of reach of children.</p><p>Avoid contact with eyes and skin.</p>
  </div>
  <div class="warning"><h5>Advarsel Warning</h5><div class="hazard"><span>!</span></div><p>Forårsager alvorlig øjenirritation. Causes serious eye irritation.</p><p>Keep out of reach of children.</p><p>UFI: 0000-0000-0000-0000</p></div>
  <div class="dosage-title">DOSERING<br>DOSAGE</div>
  <table class="dosage-table"><tr><th></th><th>soft</th><th>medium</th><th>hard</th></tr><tr><td class="size">1Kg</td><td>37 ml ≈41g</td><td>37 ml ≈61g</td><td>83 g</td></tr><tr><td class="size">5Kg</td><td>65 Kg</td><td>37 ml ≈83g</td><td>83 g</td></tr><tr><td class="size">10Kg</td><td>112 Kg</td><td>112 ml ≈124g</td><td>144g</td></tr><tr><td colspan="4">75 ml = 83g</td></tr></table>
  <div class="mini-features"><div class="feature"><div class="feature-inner">120</div></div><div class="feature"><div class="feature-inner"><svg width="9" height="9" viewBox="0 0 10 10"><circle cx="5" cy="5" r="3.6" fill="none" stroke="#fff" stroke-width="1.4"/></svg></div></div><div class="feature"><div class="feature-inner"><svg width="10" height="9" viewBox="0 0 20 18"><path d="M2 7h16l-2 9H4z M8 7l3-5 3 2" fill="none" stroke="#fff" stroke-width="1.8"/></svg></div></div></div>
  <div class="mini-temps">20°C | 30°C | 40°C | 60°C | 90°C</div>
</section>
<section class="bag bag-front variant-sand" style="left:863px;top:645px">
  <span class="hole" style="left:94px"></span><span class="hole" style="left:133px"></span><span class="hole" style="left:171px"></span>
  <div class="leaf-decor" role="img" aria-label="Faint leaf decoration"></div>
  <div class="brand-disc"><span class="brand-name">ORNE</span></div>
  <h1 class="product-title">VASKEPULVER</h1>
  <p class="product-sub">LAUNDRY DETERGENT</p>
  <div class="claim-pill">LIV OG BALANCE<br>I HVERDAGEN</div>
  <div class="feature-row"><div class="feature"><div class="feature-inner">120</div></div><div class="feature"><div class="feature-inner"><svg width="20" height="20" viewBox="0 0 10 10"><circle cx="5" cy="5" r="3.6" fill="none" stroke="#fff" stroke-width="1.4"/></svg></div></div><div class="feature"><div class="feature-inner"><svg width="24" height="22" viewBox="0 0 20 18"><path d="M2 7h16l-2 9H4z M8 7l3-5 3 2" fill="none" stroke="#fff" stroke-width="1.5"/></svg></div></div></div>
  <div class="weight-badge">10<small>kg</small></div>
  <div class="temps">20°C | 30°C | 40°C | 60°C | 90°C</div>
</section>

</body>
</html>
```